KO-TRA , Artificial hedge flyer

i need new flyer, in att i'm sending old one but as we produce artificial flowers, trees and most popular is artificial green hedge, and it's used from variety places, from swimming pool, restaurants, bars, private terrace, gardens, to protect from neighbor :-) . from beginning is all our product, it's not imported from other producer. we are doing it by measure what we get from customer ( tailor made ) , we give guaranty 15-20 years on all weather that will not loos color, etc.. you can see some pictures in att on old flyer, and some new pictures of same in space newly added. we'd like more pictures with samples of use, etc.you can see our product on www.ko-tra.hr so you can closely known what we are producing, and what for we need new flyer. we have plenty of new picture that are not on our web, so i can use it for new flyer.

Font styles to use
Sans Serif

Requirements
Must have
• company logo, contact info ( sent in word document in att ), logo of croatian product ( on old flyer in att on front side), stamp Quality since 1950 if you could change year to 1960, last time they made mistake and write 1950 ),
Nice to have
• flyer 3 fold type, or if you think it will look better only double side flyer, depend of design and theme so everyone can understand what is our business

```html
<!DOCTYPE html>
<html lang="hr">
<head>
<meta charset="utf-8">
<title>KO-TRA – letak umjetna živica</title>
<link href="https://fonts.googleapis.com/css2?family=Montserrat:wght@500;600;700&display=swap" rel="stylesheet">
<style>
  :root{
    --navy:#0b1d42;
    --navy-deep:#061230;
    --blue-edge:#0c4a9a;
    --lime:#9ccc1c;
    --lime-light:#c4e23a;
    --green:#3f9a1a;
    --green-dark:#1f5e0c;
    --white:#ffffff;
    --stage:#f2f6f3;
  }
  html,body{margin:0;padding:0;width:1200px;height:821px;overflow:hidden;background:var(--stage);}
  .stage{position:relative;width:1200px;height:821px;}
  .flyer-page{position:absolute;top:150px;width:373px;height:515px;box-shadow:0 6px 14px rgba(0,0,0,.14);}
  .flyer-page svg{display:block;width:100%;height:100%;}
  .flyer-page--front{left:187px;}
  .flyer-page--back{left:642px;}
  .brand-name{font-family:'Montserrat',sans-serif;font-weight:600;font-size:17px;fill:var(--lime);}
  .headline-small{font-family:'Montserrat',sans-serif;font-weight:500;font-size:11px;fill:var(--white);}
  .headline-large{font-family:'Montserrat',sans-serif;font-weight:700;font-size:21px;fill:var(--white);letter-spacing:.6px;}
  .intro-text{font-family:'Montserrat',sans-serif;font-weight:500;font-size:5.6px;fill:var(--white);}
  .body-text{font-family:'Montserrat',sans-serif;font-weight:600;font-size:9.4px;fill:var(--white);}
  .contact-text{font-family:'Montserrat',sans-serif;font-weight:600;font-size:6.2px;fill:var(--white);}
  .icon{fill:none;stroke:var(--white);stroke-width:1;}
  .photo-frame{fill:none;stroke:var(--navy-deep);stroke-width:6;}
</style>
</head>
<body>
<div class="stage">

  <svg width="0" height="0" style="position:absolute">
    <defs>
      <linearGradient id="pageNavy" x1="0" y1="0" x2="0" y2="1">
        <stop offset="0" stop-color="#0e2450"/><stop offset="1" stop-color="#07163a"/>
      </linearGradient>
      <linearGradient id="limeBand" x1="0" y1="0" x2="1" y2="0">
        <stop offset="0" stop-color="#6fae12"/><stop offset=".5" stop-color="#c4e23a"/><stop offset="1" stop-color="#7cb51a"/>
      </linearGradient>
      <linearGradient id="bottomBand" x1="0" y1="0" x2="1" y2="1">
        <stop offset="0" stop-color="#a6d21e"/><stop offset=".6" stop-color="#4f9a12"/><stop offset="1" stop-color="#1f5e0c"/>
      </linearGradient>
      <radialGradient id="hedgeTexture" cx=".45" cy=".5" r=".7">
        <stop offset="0" stop-color="#5ea536"/><stop offset=".6" stop-color="#3f8424"/><stop offset="1" stop-color="#1f5512"/>
      </radialGradient>
      <linearGradient id="photoDriveway" x1="0" y1="0" x2="0" y2="1">
        <stop offset="0" stop-color="#a9c3d6"/><stop offset=".3" stop-color="#8a6a50"/><stop offset=".45" stop-color="#2f5a22"/><stop offset=".75" stop-color="#2c5a1e"/><stop offset=".82" stop-color="#d8d8d2"/><stop offset="1" stop-color="#b8b8b0"/>
      </linearGradient>
      <linearGradient id="photoGreenWall" x1="0" y1="0" x2="1" y2="1">
        <stop offset="0" stop-color="#5f4a3a"/><stop offset=".35" stop-color="#3f6a2c"/><stop offset=".6" stop-color="#7a3e4a"/><stop offset="1" stop-color="#b88a5a"/>
      </linearGradient>
      <linearGradient id="photoLounger" x1="0" y1="0" x2="0" y2="1">
        <stop offset="0" stop-color="#cfe0ea"/><stop offset=".25" stop-color="#3d6e2a"/><stop offset=".6" stop-color="#2f5c20"/><stop offset=".75" stop-color="#9a8a70"/><stop offset="1" stop-color="#4a5a3a"/>
      </linearGradient>
      <linearGradient id="photoTerrace" x1="0" y1="0" x2="0" y2="1">
        <stop offset="0" stop-color="#8ea9bd"/><stop offset=".25" stop-color="#b8cfdc"/><stop offset=".45" stop-color="#2f5a22"/><stop offset=".62" stop-color="#2f5a22"/><stop offset=".72" stop-color="#9a4a24"/><stop offset="1" stop-color="#6e3218"/>
      </linearGradient>
      <linearGradient id="photoPool" x1="0" y1="0" x2="0" y2="1">
        <stop offset="0" stop-color="#7aa6d8"/><stop offset=".3" stop-color="#2d4a28"/><stop offset=".55" stop-color="#2a5a20"/><stop offset=".75" stop-color="#8a8a86"/><stop offset=".85" stop-color="#5aa7a8"/><stop offset="1" stop-color="#6e6e6a"/>
      </linearGradient>
      <linearGradient id="photoWallHedge" x1="0" y1="0" x2="0" y2="1">
        <stop offset="0" stop-color="#dfe6ea"/><stop offset=".25" stop-color="#9aa890"/><stop offset=".35" stop-color="#2f5c20"/><stop offset=".8" stop-color="#2c5a1e"/><stop offset="1" stop-color="#c8c6c0"/>
      </linearGradient>
    </defs>
  </svg>

  <!-- Front page -->
  <div class="flyer-page flyer-page--front">
    <svg viewBox="0 0 466 644" xmlns="http://www.w3.org/2000/svg">
      <defs><clipPath id="frontClip"><rect width="466" height="644"/></clipPath></defs>
      <g clip-path="url(#frontClip)">
        <rect width="466" height="644" fill="url(#pageNavy)"/>
        <path class="hedge-area" d="M0 350 C110 360 215 440 235 600 L235 644 L0 644Z" fill="url(#hedgeTexture)" role="img" aria-label="Photo of dense artificial hedge foliage"/>
        <path d="M0 185 C90 170 170 200 230 245 C300 297 380 300 466 255 L466 290 C380 332 290 318 220 268 C160 225 90 208 0 218Z" fill="url(#limeBand)"/>
        <path d="M0 218 C90 208 160 225 220 268 C290 318 380 332 466 290 L466 302 C380 342 290 328 215 276 C150 232 80 222 0 230Z" fill="var(--blue-edge)"/>
        <circle cx="324" cy="118" r="150" fill="var(--blue-edge)"/>
        <circle cx="324" cy="118" r="145" fill="url(#photoDriveway)" role="img" aria-label="Photo of artificial hedge along a driveway beside a brick house"/>
        <circle cx="106" cy="338" r="92" fill="var(--navy-deep)"/>
        <circle cx="106" cy="338" r="86" fill="url(#photoGreenWall)" role="img" aria-label="Photo of a green wall with flowers and rattan chairs"/>
        <rect x="228" y="375" width="205" height="133" rx="10" fill="url(#photoLounger)" role="img" aria-label="Photo of a hedge fence behind a garden lounger"/>
        <g class="quality-stamp">
          <circle cx="182" cy="445" r="27" fill="var(--navy-deep)"/>
          <circle cx="182" cy="445" r="25" fill="none" stroke="var(--white)" stroke-width="2"/>
          <circle cx="182" cy="445" r="19" fill="none" stroke="var(--white)" stroke-width="1"/>
          <rect x="160" y="441" width="44" height="8" fill="var(--white)"/>
        </g>
        <path d="M0 612 C100 628 190 615 250 568 C320 515 400 518 466 525 L466 644 L0 644Z" fill="url(#bottomBand)"/>
        <path d="M250 568 C320 515 400 518 466 525 L466 535 C400 528 320 528 258 575Z" fill="var(--lime-light)" opacity=".6"/>
        <circle cx="36" cy="33" r="8" fill="var(--lime)"/>
        <text class="brand-name" x="50" y="39">KO-TRA d.o.o.</text>
        <text class="headline-small" x="26" y="78">Unutarnje i vanjsko</text>
        <text class="headline-large" x="26" y="100">UREĐENJE</text>
        <text class="intro-text" x="26" y="113">poslovnih, stambenih, sportskih i</text>
        <text class="intro-text" x="26" y="120">ostalih objekata umjetnom živicom,</text>
        <text class="intro-text" x="26" y="127">dekorativnim zelenilom i cvijećem,</text>
        <text class="intro-text" x="26" y="134">drvećem i aranžmanima</text>
        <g text-anchor="end">
          <text class="body-text" x="433" y="312">Unutarnje i vanjsko uređenje poslovnih,</text>
          <text class="body-text" x="433" y="325">stambenih, sportsih i ostalih prostora</text>
          <text class="body-text" x="433" y="338">umjetnom živicom, dekorativnim zelenilom</text>
          <text class="body-text" x="433" y="351">i cvijećem, drvećem i aranžmanima</text>
          <text class="contact-text" x="420" y="569">Lipova ulica 8, ZELENJAK</text>
          <text class="contact-text" x="420" y="576">10000 Zagreb</text>
          <text class="contact-text" x="420" y="587">+385 91 400 1200</text>
          <text class="contact-text" x="420" y="597">+385 99 500 23 41</text>
          <text class="contact-text" x="420" y="607">www.ko-tra.hr</text>
          <text class="contact-text" x="420" y="617">info@ko-tra.hr</text>
        </g>
        <g class="icon">
          <path d="M429 566 a3 3 0 1 1 6 0 c0 2-3 5-3 5 s-3-3-3-5z"/>
          <path d="M429 582 l2 0 1 2-1 1 a5 5 0 0 0 2 2 l1-1 2 1 0 2 c-4 0-7-3-7-7z"/>
          <path d="M429 592 l2 0 1 2-1 1 a5 5 0 0 0 2 2 l1-1 2 1 0 2 c-4 0-7-3-7-7z"/>
          <circle cx="432" cy="605" r="3"/>
          <rect x="428.5" y="612" width="7" height="5"/>
        </g>
      </g>
    </svg>
  </div>

  <!-- Back page -->
  <div class="flyer-page flyer-page--back">
    <svg viewBox="0 0 466 644" xmlns="http://www.w3.org/2000/svg">
      <defs><clipPath id="backClip"><rect width="466" height="644"/></clipPath></defs>
      <g clip-path="url(#backClip)">
        <rect width="466" height="644" fill="url(#pageNavy)"/>
        <path class="hedge-area" d="M466 350 C360 365 250 440 232 600 L232 644 L466 644Z" fill="url(#hedgeTexture)" role="img" aria-label="Photo of dense artificial hedge foliage"/>
        <path d="M0 200 C80 240 170 262 250 222 C320 187 400 172 466 182 L466 217 C390 207 320 222 260 257 C180 302 80 292 0 242Z" fill="url(#limeBand)"/>
        <path d="M0 242 C80 292 180 302 260 257 C320 222 390 207 466 217 L466 230 C390 222 320 234 262 267 C180 312 80 302 0 254Z" fill="var(--blue-edge)"/>
        <circle cx="143" cy="118" r="150" fill="var(--blue-edge)"/>
        <circle cx="143" cy="118" r="145" fill="url(#photoTerrace)" role="img" aria-label="Photo of a wooden terrace enclosed by a hedge above the sea"/>
        <rect x="33" y="299" width="205" height="209" rx="10" fill="url(#photoPool)" role="img" aria-label="Photo of a hedge wall beside a swimming pool"/>
        <circle cx="358" cy="340" r="94" fill="var(--navy-deep)"/>
        <circle cx="358" cy="340" r="88" fill="url(#photoWallHedge)" role="img" aria-label="Photo of a hedge on a wall in front of houses"/>
        <g class="quality-stamp">
          <circle cx="284" cy="445" r="27" fill="var(--navy-deep)"/>
          <circle cx="284" cy="445" r="25" fill="none" stroke="var(--white)" stroke-width="2"/>
          <circle cx="284" cy="445" r="19" fill="none" stroke="var(--white)" stroke-width="1"/>
          <rect x="262" y="441" width="44" height="8" fill="var(--white)"/>
        </g>
        <path d="M0 530 C70 520 150 520 220 565 C290 612 390 615 466 580 L466 644 L0 644Z" fill="url(#bottomBand)"/>
        <path d="M0 530 C70 520 150 520 220 565 L212 571 C150 532 70 532 0 541Z" fill="var(--lime-light)" opacity=".6"/>
        <circle cx="300" cy="33" r="8" fill="var(--lime)"/>
        <text class="brand-name" x="314" y="39">KO-TRA d.o.o.</text>
        <text class="contact-text" x="50" y="569">Lipova ulica 8, ZELENJAK</text>
        <text class="contact-text" x="50" y="576">10000 Zagreb</text>
        <text class="contact-text" x="50" y="587">+385 91 400 1200</text>
        <text class="contact-text" x="50" y="597">+385 99 500 23 41</text>
        <text class="contact-text" x="50" y="607">www.ko-tra.hr</text>
        <text class="contact-text" x="50" y="617">info@ko-tra.hr</text>
        <g class="icon">
          <path d="M38 566 a3 3 0 1 1 6 0 c0 2-3 5-3 5 s-3-3-3-5z"/>
          <path d="M38 582 l2 0 1 2-1 1 a5 5 0 0 0 2 2 l1-1 2 1 0 2 c-4 0-7-3-7-7z"/>
          <path d="M38 592 l2 0 1 2-1 1 a5 5 0 0 0 2 2 l1-1 2 1 0 2 c-4 0-7-3-7-7z"/>
          <circle cx="41" cy="605" r="3"/>
          <rect x="37.5" y="612" width="7" height="5"/>
        </g>
      </g>
    </svg>
  </div>

</div>
</body>
</html>
```